Pathways to Brightmoor Land Ventures

size of the ad - 8”x 10.75" plus 0.25" bleed
I would like an ad for a magazine that will stand out and make people want to read the ad.
The ad should not be crowded and people reading the ad will be able to read the text.
I would like it to be a creative and modern-day design.
the list of topics should not be the focus of the ad.
the text is attached.
If you decide to use people in the ad then please no ladies.
please note that leave over 1 inch for the bottom of the footer

```html
<!DOCTYPE html>
<html lang="en">
<head>
<meta charset="utf-8">
<title>Pathways to Brightmoor Land Ventures – Course Ad</title>
<link rel="stylesheet" href="https://fonts.googleapis.com/css2?family=Anton&family=Oswald:wght@300;400;500;600&family=Montserrat:wght@500;600;800&display=swap">
<style>
  :root {
    --navy: #0c2146;
    --blue: #1f4f9c;
    --yellow: #f4e600;
    --red: #c8250b;
    --paper: #ededee;
    --band: #d4d5d8;
    --stage: #e4e4e4;
    --ink: #15223b;
  }
  * { box-sizing: border-box; margin: 0; padding: 0; }
  html, body { width: 1200px; height: 951px; overflow: hidden; background: var(--stage); }
  .canvas { position: relative; width: 1200px; height: 951px; }
  .ad {
    position: absolute; left: 260px; top: 18px; width: 681px; height: 915px;
    background: var(--paper); overflow: hidden;
    box-shadow: 0 6px 24px rgba(0,0,0,.18);
  }
  .hero { position: absolute; left: 0; top: 0; width: 100%; height: 440px; background: var(--navy); }
  .hero-title {
    position: absolute; right: 34px; top: 30px;
    font-family: "Anton", sans-serif; font-size: 70px; line-height: 1;
    color: var(--yellow); letter-spacing: 1px; white-space: nowrap;
  }
  .skyline {
    position: absolute; left: 22px; right: 22px; top: 128px; bottom: 0;
    background: linear-gradient(180deg, var(--navy) 0%, #24467e 45%, #5b7bb0 80%, #a9b9d4 100%);
  }
  .course-name {
    position: absolute; left: 22px; right: 22px; top: 452px;
    font-family: "Oswald", sans-serif; font-weight: 600; font-size: 33px; line-height: 1.1;
    color: var(--blue); text-align: right; white-space: nowrap;
  }
  .tagline {
    position: absolute; left: 22px; right: 22px; top: 502px;
    font-family: "Montserrat", sans-serif; font-weight: 800; font-size: 17px;
    color: var(--ink); text-align: right; letter-spacing: .3px; white-space: nowrap;
  }
  .info-band { position: absolute; left: 0; right: 0; top: 536px; height: 72px; background: var(--band); display: flex; }
  .location {
    width: 212px; background: var(--red); color: #fff;
    font-family: "Oswald", sans-serif; font-weight: 300; font-size: 46px;
    display: flex; align-items: center; justify-content: center;
  }
  .schedule { flex: 1; display: flex; align-items: center; padding-left: 22px; gap: 18px; }
  .sessions { display: flex; align-items: center; gap: 4px; color: var(--ink); }
  .sessions .count { font-family: "Oswald", sans-serif; font-size: 44px; font-weight: 400; line-height: 1; }
  .sessions .day { font-family: "Montserrat", sans-serif; font-weight: 500; font-size: 24px; line-height: 1; letter-spacing: 1px; }
  .sessions .unit { font-family: "Montserrat", sans-serif; font-weight: 800; font-size: 10px; color: var(--blue); letter-spacing: .5px; }
  .divider { width: 2px; height: 44px; background: var(--ink); }
  .start .date { font-family: "Montserrat", sans-serif; font-weight: 500; font-size: 22px; color: var(--ink); line-height: 1; letter-spacing: 1px; }
  .start .offer { font-family: "Montserrat", sans-serif; font-weight: 800; font-size: 15px; color: var(--blue); }
  .audience {
    position: absolute; left: 22px; right: 22px; top: 622px;
    font-family: "Oswald", sans-serif; font-weight: 500; font-size: 23px;
    color: var(--blue); text-align: center; line-height: 1.2; white-space: nowrap;
  }
  .audience .or { color: var(--ink); }
  .scholarships {
    position: absolute; left: 22px; right: 22px; top: 662px;
    font-family: "Montserrat", sans-serif; font-weight: 800; font-size: 20px;
    color: var(--red); text-align: center; letter-spacing: .5px; white-space: nowrap;
  }
  .topics {
    position: absolute; left: 30px; right: 30px; top: 708px; height: 140px;
    border: 2px solid var(--navy); border-radius: 10px;
    display: flex; justify-content: space-between; padding: 34px 28px 16px;
  }
  .topics-tab {
    position: absolute; left: 50%; top: -2px; transform: translateX(-50%);
    background: var(--navy); color: #fff; padding: 5px 26px 6px;
    border-radius: 0 0 8px 8px;
    font-family: "Montserrat", sans-serif; font-weight: 600; font-size: 14px; letter-spacing: .5px; white-space: nowrap;
  }
  .topic-list { list-style: none; font-family: "Montserrat", sans-serif; font-weight: 500; font-size: 14px; color: var(--ink); }
  .topic-list li { display: flex; align-items: flex-start; gap: 7px; margin-bottom: 5px; line-height: 1.25; }
  .topic-list svg { flex: none; margin-top: 2px; }
</style>
</head>
<body>
<div class="canvas">
  <article class="ad">
    <header class="hero">
      <div class="skyline" role="img" aria-label="Illustrated night city skyline of lit high-rise towers"></div>
      <h1 class="hero-title">REAL ESTATE COURSE</h1>
    </header>

    <h2 class="course-name">PATHWAYS TO BRIGHTMOOR LAND VENTURES</h2>
    <p class="tagline">INVESTING IN KNOWLEDGE IS INVESTING IN OPPORTUNITIES</p>

    <section class="info-band">
      <div class="location">ELMRIDGE</div>
      <div class="schedule">
        <div class="sessions">
          <span class="count">10</span>
          <span><span class="day">TUESDAY</span><br><span class="unit">EVENINGS SESSIONS</span></span>
        </div>
        <div class="divider"></div>
        <div class="start">
          <div class="date">STARTING FEB.28</div>
          <div class="offer">EARLY BIRD SPECIAL</div>
        </div>
      </div>
    </section>

    <p class="audience">FOR THOSE THAT STARTED <span class="or">OR</span> WOULD LIKE TO GO INTO REAL ESTATE</p>
    <p class="scholarships">LIMITED PARTIAL SCHOLARSHIPS</p>

    <section class="topics">
      <div class="topics-tab">TOPICS: PARTIAL LISTING</div>
      <svg width="0" height="0" style="position:absolute">
        <symbol id="tick" viewBox="0 0 12 12">
          <circle cx="6" cy="6" r="6" fill="#1f4f9c"/>
          <path d="M3.2 6.2 L5.2 8.1 L8.9 4.2" fill="none" stroke="#fff" stroke-width="1.6" stroke-linecap="round" stroke-linejoin="round"/>
        </symbol>
      </svg>
      <ul class="topic-list">
        <li><svg width="12" height="12"><use href="#tick"/></svg>Real estate investment<br>strategies</li>
        <li><svg width="12" height="12"><use href="#tick"/></svg>Property management</li>
        <li><svg width="12" height="12"><use href="#tick"/></svg>Real estate Legal basics</li>
      </ul>
      <ul class="topic-list">
        <li><svg width="12" height="12"><use href="#tick"/></svg>Due diligence</li>
        <li><svg width="12" height="12"><use href="#tick"/></svg>Financing</li>
        <li><svg width="12" height="12"><use href="#tick"/></svg>Underwriting</li>
        <li><svg width="12" height="12"><use href="#tick"/></svg>Syndication</li>
      </ul>
      <ul class="topic-list">
        <li><svg width="12" height="12"><use href="#tick"/></svg>Sourcing deals</li>
        <li><svg width="12" height="12"><use href="#tick"/></svg>Dealing with brokers</li>
        <li><svg width="12" height="12"><use href="#tick"/></svg>Tax fundamentals</li>
      </ul>
    </section>
  </article>
</div>
</body>
</html>
```